Personal Finance Author needs a postcard

Hi there,

I am a Canadian personal finance author and have published a new book called The Wealth Compass.

I teach Millennials how to create a 6-figure portfolio through investing (https://www.dariafelt.com/)

I'm speaking at some conferences so we were going to print some postcards to hand out to attendees with our info and calls-to-action on them.

I am looking for 4x6 (horizontal) postcard (no space needed for shipping label).

Logos, Headshots and Book Cover:
https://files.cloudvaultex.com/folders/8kQpZrT2mWvN4xLbJ7sHdYc3FgA9eUoRi?usp=sharing

Both sides will be full colour. I would like a clean and simple look. Our main sites are www.DariaFelt.com and www.TheWealthCompassBook.com if you want to get a sense of style and design.
I also uploaded a few marketing materials so you can see the existing designs.

Side 1:
Get Instant Access to your Free Resources - main headline

(small bullets underneath)
- The Wealth Compass Checklist
- Financial Worksheets
- Database of Investment Tools

DariaFelt.com/Resources

At the bottom, include "Don't forget to follow Daria Felt on social media:
Linkedin: @dariafelt7
Facebook: @thewealthcompassbook Instagram: @thewealthcompassbook Twitter: @WealthCompassBk"

Side 2:
Headline - Want to work directly with Daria and The Wealth Compass team to help you make your money grow and stay safe?

Work with us to (bullet point list)...
- Hire Daria as a Keynote Speaker
- Teach Financial Literacy Workshops
- Receive Financial Coaching

Want To Learn More About How We Can Help?
DariaFelt.com/Services

Include my contact info:
Daria Felt
Author | Speaker | Investor
daria@thewealthcompassbook.com
416-555-0187

Target Market(s)

Millennials who want to learn how to save and invest their money. I focus on stock market investing, real estate investing and entrepreneurship.

Industry/Entity Type

Financial Service

Font styles to use
Sans Serif

Colors

Designer to choose colors to be used in the design.

Requirements
Must have
• Photo of Daria Felt
• The Wealth Compass logo
• Green, Gold/Yellow to match existing colours
• modern business style postcard

```html
<!DOCTYPE html>
<html lang="en">
<head>
<meta charset="utf-8">
<title>The Wealth Compass – Postcard</title>
<link rel="stylesheet" href="https://fonts.googleapis.com/css2?family=Encode+Sans+Semi+Condensed:wght@400;600;700&display=swap">
<style>
  :root {
    --green: #066b2e;
    --gold: #f4c21b;
    --ink: #1b1b1b;
    --paper: #ffffff;
    --backdrop: #f3efcf;
    --photo-light: #e9e4de;
    --photo-dark: #2a2a2e;
  }
  * { margin: 0; padding: 0; box-sizing: border-box; }
  html, body { width: 1200px; height: 900px; overflow: hidden; }
  body {
    background: var(--backdrop);
    font-family: "Encode Sans Semi Condensed", "Arial Narrow", sans-serif;
    position: relative;
  }
  .postcard {
    position: absolute;
    width: 600px; height: 400px;
    background: var(--paper);
    overflow: hidden;
    box-shadow: 0 2px 6px rgba(0,0,0,.18);
  }
  .postcard--front { left: 40px; top: 40px; }
  .postcard--back { left: 560px; top: 460px; }
  .postcard__bands { position: absolute; inset: 0; }

  .brand-mark {
    position: absolute;
    color: var(--green);
    font-weight: 700;
    text-transform: uppercase;
    line-height: .95;
    letter-spacing: .5px;
  }
  .postcard--front .brand-mark { left: 30px; top: 62px; font-size: 30px; }
  .postcard--back .brand-mark { left: 20px; top: 28px; font-size: 17px; }

  .headshot {
    position: absolute;
    left: 30px; top: 150px;
    width: 165px; height: 170px;
    background: linear-gradient(180deg, var(--photo-light) 0%, var(--photo-light) 45%, var(--photo-dark) 100%);
  }

  .headline {
    position: absolute;
    right: 40px; top: 46px;
    text-align: right;
    color: var(--green);
    font-weight: 700;
    font-size: 31px;
    line-height: 1.08;
  }
  .resource-list {
    position: absolute;
    right: 40px; top: 190px;
    list-style: none;
    text-align: right;
    color: var(--ink);
    font-weight: 600;
    font-size: 17px;
    line-height: 26px;
  }
  .resource-list li::after {
    content: "";
    display: inline-block;
    width: 7px; height: 7px;
    margin-left: 9px;
    border-radius: 50%;
    background: var(--ink);
    vertical-align: middle;
  }

  .social {
    position: absolute;
    left: 0; right: 0; top: 334px;
    color: var(--paper);
    text-align: center;
  }
  .social__title { font-weight: 600; font-size: 16px; }
  .social__handles {
    display: flex; justify-content: center; align-items: center;
    margin-top: 12px;
    list-style: none;
    font-size: 12px;
    font-weight: 600;
  }
  .social__handles li { display: flex; align-items: center; padding: 0 8px; }
  .social__handles li + li { border-left: 1.5px solid var(--paper); }
  .social__handles li::before {
    content: "";
    width: 17px; height: 17px;
    margin-right: 5px;
    border-radius: 50%;
    background: var(--paper);
  }

  .services {
    position: absolute;
    left: 20px; top: 82px;
    width: 290px;
  }
  .services__headline {
    color: var(--green);
    font-size: 14.5px;
    line-height: 21px;
  }
  .services__intro { margin-top: 16px; font-size: 12.5px; color: var(--ink); }
  .services__list {
    margin-top: 4px;
    list-style: none;
    font-size: 10.5px;
    line-height: 16px;
    color: var(--ink);
  }
  .services__list li::before {
    content: "";
    display: inline-block;
    width: 4px; height: 4px;
    margin-right: 7px;
    border-radius: 50%;
    background: var(--ink);
    vertical-align: middle;
  }

  .contact {
    position: absolute;
    left: 20px; top: 270px;
    color: var(--ink);
    font-weight: 600;
  }
  .contact__name { font-size: 15.5px; line-height: 20px; }
  .contact__line { font-size: 13px; line-height: 18px; }
  .contact__more { font-size: 11.5px; font-weight: 400; margin-top: 2px; }
  .contact__url { font-size: 9.5px; font-weight: 400; }

  .mail-divider {
    position: absolute;
    left: 318px; top: 24px;
    width: 2px; height: 346px;
    background: var(--ink);
  }
  .stamp-box {
    position: absolute;
    left: 505px; top: 22px;
    width: 63px; height: 80px;
    border: 1.5px solid var(--ink);
  }
  .address-lines {
    position: absolute;
    left: 346px; top: 270px;
    width: 222px;
  }
  .address-lines span {
    display: block;
    height: 1.5px;
    background: var(--ink);
    margin-bottom: 24px;
  }
</style>
</head>
<body>

<section class="postcard postcard--front" aria-label="Postcard front">
  <svg class="postcard__bands" viewBox="0 0 600 400" width="600" height="400" aria-hidden="true">
    <path d="M0 0 H600 V42 Q300 -6 0 52 Z" fill="var(--green)"/>
    <path d="M0 54 Q300 0 600 46" fill="none" stroke="var(--gold)" stroke-width="3"/>
    <path d="M0 318 Q330 350 600 295 V400 H0 Z" fill="var(--green)"/>
    <path d="M0 318 Q330 350 600 295" fill="none" stroke="var(--gold)" stroke-width="3"/>
  </svg>

  <div class="brand-mark">The<br>Wealth<br>Compass</div>
  <div class="headshot" role="img" aria-label="Portrait photo of Daria Felt in a dark blazer"></div>

  <h1 class="headline">Get Instant Access<br>to your Free Resources</h1>
  <ul class="resource-list">
    <li>The Wealth Compass Checklist</li>
    <li>Financial Worksheets</li>
    <li>Database of Investment Tools</li>
  </ul>

  <div class="social">
    <p class="social__title">Follow Daria Felt on social media</p>
    <ul class="social__handles">
      <li>@dariafelt7</li>
      <li>@thewealthcompassbook</li>
      <li>@WealthCompassBk</li>
      <li>@thewealthcompassbook</li>
    </ul>
  </div>
</section>

<section class="postcard postcard--back" aria-label="Postcard back">
  <svg class="postcard__bands" viewBox="0 0 600 400" width="600" height="400" aria-hidden="true">
    <path d="M0 0 H600 V22 Q300 2 0 12 Z" fill="var(--green)"/>
    <path d="M0 14 Q300 4 600 24" fill="none" stroke="var(--gold)" stroke-width="2.5"/>
    <path d="M0 366 Q330 396 600 352 V400 H0 Z" fill="var(--green)"/>
    <path d="M0 366 Q330 396 600 352" fill="none" stroke="var(--gold)" stroke-width="2.5"/>
  </svg>

  <div class="brand-mark">The Wealth<br>Compass</div>

  <div class="services">
    <p class="services__headline">Want to work directly with Daria and The Wealth Compass team to help you make your money grow and stay safe?</p>
    <p class="services__intro">Work with us to</p>
    <ul class="services__list">
      <li>Hire Daria as a Keynote Speaker</li>
      <li>Teach Financial Literacy Workshops</li>
      <li>Receive Financial Coaching</li>
    </ul>
  </div>

  <div class="contact">
    <p class="contact__name">Daria Felt</p>
    <p class="contact__line">Author | Speaker | Investor</p>
    <p class="contact__line">daria@thewealthcompassbook.com</p>
    <p class="contact__line">416-555-0187</p>
    <p class="contact__more">To Learn More</p>
    <p class="contact__url">DariaFelt.com/Services</p>
  </div>

  <div class="mail-divider"></div>
  <div class="stamp-box"></div>
  <div class="address-lines"><span></span><span></span><span></span><span></span></div>
</section>

</body>
</html>
```